INNOVATIVE DESIGN NEEDED FOR FINANCIAL COMPANY

INTERNATIONAL FIRM IN HONG KONG NEEDS A MODERN BUSINESS CARD DESIGN. ONE SIDE ENGLISH OTHER SIDE IN CHINESE. WE ARE OPEN TO CHANGING FONTS AND COLOR. SHOULD BE A CARD THAT IS PROFESSIONAL DEALING WITH HIGH NET WORTH CLIENTELE. BOTH SIDES OF THE CARD WILL BE THE SAME, HOWEVER, THE WORDING ON ONE SIDE WILL BE ENGLISH AND THE OTHER SIDE IN CHINESE (CAN ASSIST IN THE LETTERING - CAN PROVIDE ONCE CARD DESIGN IS ACCEPTED.

Target Market(s)

Hong Kong/CHINA

Contact Information for Business Card

ATTRACTIVE MODERN

```html
<!DOCTYPE html>
<html lang="en">
<head>
<meta charset="utf-8">
<title>Evergate Asset Management – Business Cards</title>
<link href="https://fonts.googleapis.com/css2?family=Roboto:wght@400;500;700&family=Noto+Sans+TC:wght@400;700&display=swap" rel="stylesheet">
<style>
  :root {
    --bg: #dcdcdc;
    --card: #ffffff;
    --green: #17906a;
    --green-light: #1f9b76;
    --dark: #444444;
    --ink: #4a4a4a;
    --on-green: #ffffff;
  }
  * { margin: 0; padding: 0; box-sizing: border-box; }
  html, body { width: 1200px; height: 1200px; overflow: hidden; background: var(--bg); }
  body { position: relative; font-family: "Roboto", "Noto Sans TC", sans-serif; }

  .card {
    position: absolute;
    left: 257px;
    width: 800px;
    height: 457px;
    background: var(--card);
    overflow: hidden;
    transform: scale(0.8571);
    transform-origin: 0 0;
    box-shadow: 0 18px 30px rgba(0,0,0,0.25);
  }
  .card--english { top: 165px; }
  .card--chinese { top: 653px; }

  .wave { position: absolute; inset: 0; width: 800px; height: 457px; }

  .brand { position: absolute; left: 52px; top: 88px; display: flex; align-items: center; gap: 14px; }
  .brand__dot { width: 60px; height: 60px; border-radius: 50%; background: var(--green); }
  .brand__name { color: var(--ink); font-weight: 700; line-height: 1; }
  .brand__zh { font-family: "Noto Sans TC", sans-serif; font-size: 24px; letter-spacing: 3px; }
  .brand__en { font-family: "Roboto", sans-serif; font-size: 12.5px; letter-spacing: 1.6px; margin-top: 5px; }

  .details {
    position: absolute;
    right: 43px;
    top: 210px;
    text-align: right;
    color: var(--on-green);
  }
  .details__name { font-size: 30px; font-weight: 700; line-height: 1.05; }
  .details__title { font-size: 20px; font-weight: 500; line-height: 1.3; }
  .details__address { font-size: 19px; line-height: 24px; margin-top: 16px; }
  .details__contacts { list-style: none; margin-top: 14px; font-size: 19px; line-height: 26px; }
  .details__contacts li { display: flex; justify-content: flex-end; align-items: center; gap: 6px; }
  .details__contacts svg { width: 17px; height: 17px; fill: var(--on-green); }

  .card--chinese .details { top: 212px; }
  .card--chinese .details__name { font-family: "Noto Sans TC", sans-serif; font-weight: 400; font-size: 30px; letter-spacing: 1px; }
  .card--chinese .details__title { font-family: "Noto Sans TC", sans-serif; font-weight: 400; font-size: 20px; margin-top: 8px; }
  .card--chinese .details__address { margin-top: 8px; }
</style>
</head>
<body>

<svg width="0" height="0" style="position:absolute">
  <defs>
    <linearGradient id="greenFill" x1="0" y1="0" x2="0" y2="1">
      <stop offset="0" stop-color="#1f9b76"/>
      <stop offset="1" stop-color="#138c66"/>
    </linearGradient>
    <symbol id="icon-phone" viewBox="0 0 24 24"><path d="M6.6 10.8a15.1 15.1 0 0 0 6.6 6.6l2.2-2.2a1 1 0 0 1 1-.25 11.4 11.4 0 0 0 3.6.57 1 1 0 0 1 1 1V20a1 1 0 0 1-1 1A17 17 0 0 1 3 4a1 1 0 0 1 1-1h3.5a1 1 0 0 1 1 1c0 1.25.2 2.45.57 3.6a1 1 0 0 1-.25 1z"/></symbol>
    <symbol id="icon-mail" viewBox="0 0 24 24"><path d="M2 5h20v14H2z M3.5 6.5 12 13l8.5-6.5" fill="none" stroke="#fff" stroke-width="2"/></symbol>
    <symbol id="icon-globe" viewBox="0 0 24 24"><circle cx="12" cy="12" r="10"/><path d="M7 7c2 1 3 3 2 5s1 3 0 5M15 4c-1 2 1 3 3 3M14 14c2 0 3 2 2 4" fill="none" stroke="#17906a" stroke-width="2"/></symbol>
  </defs>
</svg>

<section class="card card--english" lang="en">
  <svg class="wave" viewBox="0 0 800 457" aria-hidden="true">
    <path d="M0,308 C120,385 270,402 385,318 C505,228 580,118 700,90" fill="none" stroke="var(--dark)" stroke-width="22"/>
    <path d="M230,405 C300,400 350,380 420,320 C540,215 600,110 700,88" fill="none" stroke="var(--green)" stroke-width="3"/>
    <path d="M0,338 C120,405 260,415 385,330 C515,238 600,100 725,97 C760,97 790,110 800,118 L800,457 L0,457Z" fill="url(#greenFill)"/>
  </svg>
  <div class="brand">
    <span class="brand__dot"></span>
    <div class="brand__name">
      <div class="brand__zh">恒峰資產管理有限公司</div>
      <div class="brand__en">Evergate Asset Management Ltd</div>
    </div>
  </div>
  <div class="details">
    <div class="details__name">Daniel Wong</div>
    <div class="details__title">President</div>
    <div class="details__address">2108 Maple Crest Lane<br>Kowloon Bay, Hong Kong</div>
    <ul class="details__contacts">
      <li>555-214-7730 <svg><use href="#icon-phone"/></svg></li>
      <li>info@evergateam.com <svg><use href="#icon-mail"/></svg></li>
      <li>www.evergateam.com <svg><use href="#icon-globe"/></svg></li>
    </ul>
  </div>
</section>

<section class="card card--chinese" lang="zh-Hant">
  <svg class="wave" viewBox="0 0 800 457" aria-hidden="true">
    <path d="M0,308 C120,385 270,402 385,318 C505,228 580,118 700,90" fill="none" stroke="var(--dark)" stroke-width="22"/>
    <path d="M230,405 C300,400 350,380 420,320 C540,215 600,110 700,88" fill="none" stroke="var(--green)" stroke-width="3"/>
    <path d="M0,338 C120,405 260,415 385,330 C515,238 600,100 725,97 C760,97 790,110 800,118 L800,457 L0,457Z" fill="url(#greenFill)"/>
  </svg>
  <div class="brand">
    <span class="brand__dot"></span>
    <div class="brand__name">
      <div class="brand__zh">恒峰資產管理有限公司</div>
      <div class="brand__en">Evergate Asset Management Ltd</div>
    </div>
  </div>
  <div class="details">
    <div class="details__name">丹尼尔黄</div>
    <div class="details__title">主席</div>
    <div class="details__address">2108 Maple Crest Lane<br>九龍灣, 香港</div>
    <ul class="details__contacts">
      <li>555-214-7730 <svg><use href="#icon-phone"/></svg></li>
      <li>info@evergateam.com <svg><use href="#icon-mail"/></svg></li>
      <li>www.evergateam.com <svg><use href="#icon-globe"/></svg></li>
    </ul>
  </div>
</section>

</body>
</html>
```